Arizona Pool Company Brochure

**** UPDATE 2-8-2014 ****

Size should be 11" X 17" or larger (tri or bi fold).

We're going to let the contest run it's full duration to allow for more time spent on designs.

No black backgrounds.

Consideration should be given to having the text be easy to read and in a nice, organized format.

*****************************

We're looking for an eye-catching, colorful brochure that will explain what we do, who we are... and what sets us apart from the competition.

Our company provides swimming pool service, repair, and custom renovations throughout the Phoenix, Arizona metropolitan area. These brochures will be hand-delivered to each prospective customer we visit.

The brochure will include images of our work, product logos, and a unique design that separates our company apart from the rest.

The brochure should be tri-fold. Although, if a designer wants to (or has better ideas) for a different lay-out, then we're open to seeing what can be done.

Colors we like: Blue, White, Silver, Copper, Green (accent color)

We like designs that are unique/different. Professional. Creative. Sleek. Sexy. Custom. We don't want the brochure to be "pretentious". We'd like for these brochures to leave a lasting impression with our prospective clients... and hopefully earn us more business.

We don't want the brochure to be too wordy, however if the designer feels we need to cut back (or add), let us know.

Our motto is "Every Wave Stays Bright".

You can view some of our projects, and what we're about either at our website (tidewellaqua.com), Chatterbook (www.facebook/tidewellaqua), or Searchly+ (https://plus.google.com/+Tidewellaqua). Thank you!

- Print-

(Front) Logo

Service - Repair - Renovation
480-555-0147
tidewellaqua.com
service@tidewellaqua.com
Like Us On Chatterbook! Chatterbook LOGO
Searchly Circle LOGO

(Body) Why Choose Us?

Thank you for the opportunity for our company to become your pool service provider!

We’re committed to providing the best customer service possible! At the end of the day you want your pool to be clean, clear, operational, and for your service provider to be available when you need them!

We’re licensed with the Desert State Builders Licensing Office, Bonded, and Fully Insured.
A+ reviews with the Fair Trade Merchants Council, Marlo's Roster, Vetchly, Ornu, Chatterbook, and Searchly!
All technicians are employees... not sub-contractors! Our employees are hard working, dependable, professional, and expected to follow our strict protocol for servicing your pool.
Flat-fee service rates! Any additional equipment repairs, maintenance, or chemical implementations are directly authorized by you!
No contracts! Our Service Level Agreement Form allows you to select your desired level of authorization for equipment repairs, filter maintenance, and extra chemical implementation programs.
Our uniformed technicians arrive in distinctive, clean GPS-tracked company trucks.
We leave detailed service slips after each service visit. In addition, all service visit information is electronically recorded and stored.
Easy, online account management to view and pay invoices or authorize estimates.
Invoices, estimates, questions, pictures, and video are communicated via e-mail!
Free service calls to diagnose equipment issues outside of our normal service.
10% Service Client Discount for all repairs and replacement items.
Tidewell Aqua Service knows the importance of communication! We’re available by phone, email, or text all days of the week.

(Body) Our Methodology

We believe in 5 important factors in maintaining a clean, clear, and operational pool...

Good, Clean Water! Our local water supply contains high amounts of minerals. Pool chemicals add to this problem in a short amount of time. Our philosophy is to use the least amount of chemicals possible to achieve optimal water balance.
Efficient Water Flow! The invention of variable-speed pumps has enabled the ability to "dial in" proper water flow... while driving down energy costs.
Proper Filtration! Today’s high-capacity cartridge filters provide great filtration, save on wasted water from backwashing sand filters, and eliminate the need for water flow-restricting backwash valves.
Functioning Cleaning System! Having a working automatic cleaning system is vital in keeping the pool surface clean of debris and dirt... and free of staining.
A Dependable And Professional Pool Maintenance Technician! Our job is to not only oversee all of the items listed above... but to make sure your pool is in the best condition possible!

(Body) Equipment Repair & Installation

We’re educated on all phases of swimming pool equipment repair and installation... with a focus on energy-efficiency and optimum performance!

We’re an KVE & BTU Authorized Installer of variable-speed pool pumps. KVE & BTU trust us to properly install and calibrate all variable-speed pumps. We've been equipped to handle the new industry standards on variable-speed pumps since Arizona law went into effect January 1st, 2011.
We’re experts at acid washes and erasing the mineral build-up off of waterlines. All work is done in-house with our customized cleaning rig and trailer.
Heating systems. New efficiency standards have made installation and operation more affordable than ever.
Remote control automation systems. Technology now allows the user to easily view and control their entire pool system via a remote home computer, tablet, or phone!
Brilliant, color-changing LED lighting for pools and spas! The benefits of LED include brighter and broader displays... while lasting much longer than your typical light bulbs.
Salt systems provide a soft-water experience! In addition to the benefit of better feeling water, salt systems generate plenty of chlorine to keep your pool sanitized.

(Body) About Us

A native to Phoenix, Darren Whitcombe founded Tidewell Aqua Service in 2000. Our company was built from the ground up by way of hard work, word of mouth, and determination. Our company will always remain firmly grounded, and continue to develop systems that put our customers first!

Our philosophy is to treat every pool as if it were our own, run an efficient and organized business, and care for our employees.

Tidewell Aqua Service is a yearly, proud contributor to the Saguaro Youth Medical Center Splash Smart Day. Please educate and watch all children around water... every accident can be avoided.

(Back) Contact Us
Logos To Use, Files Uploaded: Marlo's Roster, FTMC, Quorvix, Searchly+, Chatterbook, KVE/BTU logo, Saguaro Youth Medical Center

Office: 480-555-0147 | Fax: 480-555-0193 | Email: service@tidewellaqua.com
tidewellaqua.com

Office / Warehouse Location
41762 East Kettle Lane, Suite 7
Phoenix, Arizona 85000
(NW of Kettle Lane & Mesquite Ridge Drive)

AZ ROC: 731402, 731403, 731404, 605218

Target Market(s)

We target a market of pool owners, which typically have more disposable income.

30 - 75 years old.

Our clients range from first-time home buyers, self-employed, business professionals, doctors, landlords, thousandaires, millionaires.

Industry/Entity Type

Pool Service

Font styles to use
Serif

Colors
0355a3
cfdfed
ffffff
3176b5
eaf1f7

Requirements
Must have
• Must use provided images. We've included a few pool pictures, and will let you decide which ones to incorporate throughout the brochure.

Logos Used:
Tidewell Aqua Service
Quorvix
FTMC
Marlo's Roster
KVE
BTU
Saguaro Youth Medical Center
Searchly+
Chatterbook

Image pic of some of our trucks.

Nice to have
• Equipment images worked in.
Should not have
• Cartoonish fonts or design. No "Love" hearts!!

```html
<!DOCTYPE html>
<html lang="en">
<head>
<meta charset="utf-8">
<title>Tidewell Aqua Service Brochure</title>
<link rel="stylesheet" href="https://fonts.googleapis.com/css2?family=Source+Sans+3:wght@400;600;700&display=swap">
<style>
  :root {
    --navy: #2b2a6b;
    --brand-blue: #0355a3;
    --mid-blue: #3176b5;
    --sky-blue: #4f95d8;
    --pale-blue: #cfdfed;
    --mist: #eaf1f7;
    --white: #ffffff;
    --green: #8cc63f;
    --ink: #111111;
  }
  * { box-sizing: border-box; margin: 0; padding: 0; }
  html, body { width: 1200px; height: 777px; overflow: hidden; background: var(--brand-blue); }
  body { font-family: "Source Sans 3", Arial, sans-serif; }
  .brochure { position: relative; width: 1200px; height: 777px; overflow: hidden; }

  .photo { position: absolute; }
  .photo-garden {
    left: 400px; top: 400px; width: 700px; height: 377px;
    background: linear-gradient(160deg, #9ea96a 0%, #a88a6a 25%, #c98fa8 42%, #7fb4c6 62%, #2f8fb0 85%, #1f6f98 100%);
  }
  .photo-desert {
    left: 800px; top: 0; width: 400px; height: 340px;
    background: linear-gradient(180deg, #d9dde0 0%, #b9c3cb 28%, #7f9a72 45%, #4e9aa8 62%, #a99478 80%, #8a7a62 100%);
  }
  .contact-sheet { position: absolute; left: 400px; top: 0; width: 400px; height: 400px; background: var(--white); }

  .waves { position: absolute; inset: 0; width: 1200px; height: 777px; }

  .why-panel { position: absolute; left: 0; top: 0; width: 395px; color: var(--white); }
  .why-title { position: absolute; left: 0; top: 32px; width: 365px; text-align: center; color: var(--green); font-size: 24px; font-weight: 700; }
  .why-intro { position: absolute; left: 32px; top: 65px; width: 345px; font-size: 12.5px; font-weight: 700; line-height: 14.5px; }
  .why-list { position: absolute; left: 32px; top: 118px; width: 335px; list-style: none; }
  .why-list li { position: relative; padding-left: 18px; font-size: 13.2px; line-height: 15.5px; margin-bottom: 11.5px; }
  .why-list li::before { content: ""; position: absolute; left: 0; top: 4px; width: 10px; height: 10px; border-radius: 50%; background: var(--green); }

  .contact-title { position: absolute; left: 430px; top: 28px; width: 400px; text-align: center; font-size: 22px; font-weight: 700; color: var(--ink); }
  .contact-grid { position: absolute; left: 520px; top: 64px; display: grid; grid-template-columns: 64px auto; column-gap: 6px; font-size: 15px; line-height: 19px; color: var(--ink); }
  .contact-grid dt { text-align: right; }
  .location { position: absolute; left: 481px; top: 158px; font-size: 15px; line-height: 18.5px; color: var(--ink); font-style: normal; }
  .location h3 { font-size: 15px; font-weight: 700; }
  .location .roc { font-size: 13.5px; padding-left: 3px; }
  .like-title { position: absolute; left: 452px; top: 260px; font-size: 19px; font-weight: 700; color: var(--ink); }
  .partner { position: absolute; font-size: 15px; font-weight: 700; color: var(--brand-blue); display: flex; align-items: center; gap: 5px; line-height: 16px; }
  .partner .mark { width: 12px; height: 12px; background: var(--brand-blue); flex: none; }
  .partner-badge { position: absolute; left: 690px; top: 295px; width: 55px; height: 55px; border-radius: 50%; background: var(--green); }

  .brand { position: absolute; left: 850px; top: 360px; width: 335px; text-align: right; }
  .brand-name { font-size: 44px; font-weight: 700; color: var(--brand-blue); line-height: 44px; }
  .brand-tag { font-size: 16px; font-weight: 700; color: var(--brand-blue); margin-top: 2px; }

  .services { position: absolute; left: 822px; top: 723px; line-height: 24px; transform-origin: left center; transform: rotate(-42deg); color: var(--white); font-size: 20px; font-weight: 700; letter-spacing: 1px; white-space: nowrap; }
  .front-contact { position: absolute; right: 35px; top: 636px; text-align: right; color: var(--white); font-size: 20px; line-height: 27.5px; }
</style>
</head>
<body>
<main class="brochure">
  <div class="photo photo-garden" role="img" aria-label="Photo of a rock waterfall pool with flowering planter and blue water"></div>
  <div class="photo photo-desert" role="img" aria-label="Photo of a desert pool and spa with stone decking under a cloudy sky"></div>
  <div class="contact-sheet"></div>

  <svg class="waves" viewBox="0 0 1200 777" aria-hidden="true">
    <path d="M0 0 H445 C418 180 425 420 440 560 C450 650 430 730 420 777 H0 Z" fill="var(--sky-blue)"/>
    <path d="M0 0 H425 C400 190 405 420 420 560 C430 650 410 720 400 777 H0 Z" fill="var(--mid-blue)"/>
    <path d="M0 0 H410 C385 200 388 420 402 560 C410 640 398 720 390 777 H0 Z" fill="var(--navy)"/>
    <path d="M0 735 C120 715 260 720 400 760 V777 H0 Z" fill="var(--mid-blue)"/>
    <path d="M800 300 C950 290 1080 255 1200 230 V265 C1080 290 950 320 800 328 Z" fill="var(--brand-blue)"/>
    <path d="M800 322 C950 315 1080 285 1200 258 V288 C1080 310 950 335 800 346 Z" fill="var(--green)"/>
    <path d="M800 342 C950 332 1080 305 1200 282 V428 C1100 432 1050 452 1030 475 L800 475 Z" fill="var(--white)"/>
    <path d="M800 330 C860 345 860 420 840 462 C890 446 960 448 1035 472 L1030 480 L800 480 Z" fill="var(--brand-blue)"/>
    <path d="M1200 425 C1100 432 1050 452 1030 475 C970 545 870 620 800 660 V777 H1200 Z" fill="var(--brand-blue)"/>
    <path d="M1200 434 C1110 442 1065 462 1045 490 C1065 474 1110 462 1200 456 Z" fill="var(--mid-blue)"/>
  </svg>

  <section class="why-panel">
    <h2 class="why-title">Why Choose Us</h2>
    <p class="why-intro">Thank you for the opportunity for our company to become your pool service provider!&nbsp; We’re committed to providing the best customer service&nbsp; possible!</p>
    <ul class="why-list">
      <li>We’re licensed with the Desert State Builders Licensing Office, Bonded, and Fully Insured.</li>
      <li>A+ reviews with the Fair Trade Merchants Council, Marlo's Roster, Vetchly, Ornu, Chatterbook, and Searchly!</li>
      <li>All technicians are employees... not sub-contractors! Our employees are hardworking, dependable, professional, and expected to follow our strict protocol for servicing your pool.</li>
      <li>Flat-fee service rates! Any additional equipment repairs, maintenance, or chemical implementations are directly authorized by you!</li>
      <li>No contracts! Our Service Level Agreement Form allows you to select your desired level of authorization for equipment repairs, filter maintenance, and extra chemical implementation programs.</li>
      <li>Our uniformed technicians arrive in distinctive, clean GPS-tracked company trucks.</li>
      <li>We leave detailed service slips after each service visit. In addition, all service visit information is electronically recorded and stored.</li>
      <li>Easy, online account management to view and pay invoices or authorize estimates.</li>
      <li>Invoices, estimates, questions, pictures, and video are communicated via e-mail!</li>
      <li>Free service calls to diagnose equipment issues outside of our normal service.</li>
      <li>10% Service Client Discount for all repairs and replacement items.</li>
      <li>Tidewell Aqua Service knows the importance of communication! We’re available by phone, email, or text all days of the week.</li>
    </ul>
  </section>

  <h2 class="contact-title">Contact Us</h2>
  <dl class="contact-grid">
    <dt>Office:</dt><dd>480-555-0147</dd>
    <dt>Fax:</dt><dd>480-555-0193</dd>
    <dt>Email:</dt><dd>service@tidewellaqua.com</dd>
    <dt></dt><dd>tidewellaqua.com</dd>
  </dl>
  <address class="location">
    <h3>Office / Warehouse Location</h3>
    41762 East Kettle Lane, Suite 7<br>
    Phoenix, Arizona 85000<br>
    (NW of Kettle Lane &amp; Mesquite Ridge Drive)<br>
    <span class="roc">AZ ROC: 731402, 731403, 731404, 605218</span>
  </address>

  <h3 class="like-title">Like US On :</h3>
  <span class="partner" style="left:452px;top:306px"><span class="mark"></span>Chatterbook</span>
  <span class="partner" style="left:560px;top:330px">Searchly+</span>
  <span class="partner" style="left:600px;top:300px">BTU</span>
  <span class="partner-badge"></span>
  <span class="partner" style="left:452px;top:350px;width:115px">Saguaro Youth Medical Center</span>
  <span class="partner" style="left:600px;top:354px;font-size:22px;line-height:24px">KVE</span>

  <div class="brand">
    <div class="brand-name">tidewellaqua</div>
    <div class="brand-tag">Every Wave Stays Bright</div>
  </div>

  <div class="services">SERVICE - REPAIR - RENOVATION</div>
  <div class="front-contact">
    480-555-0147<br>
    480-555-0193<br>
    tidewellaqua.com<br>
    service@tidewellaqua.com
  </div>
</main>
</body>
</html>
```